Drone service provider needs a brilliant web design

I need a responsive web design for a new drone service company. Pelwick Drone Solutions provides turnkey solutions to capture, process, and deliver actionable aerial data to customers. The design should communicate a professional company that is safe, legal and insured. I included our logo design and business card designs for reference.
*content to be supplied after design selected

Target Market(s)

We serve telecommunications, construction, government, utility infrastructure, insurance and other industries.

Industry/Entity Type

Industrial

Number of Pages Required

5+ page

Colors

Designer to choose colors to be used in the design.

Requirements
Must have
• The design should highlight professional services to include Inspections, Mapping, Consulting and Training. The site should include aerial images and video to compliment the services offered. The landing page must include following sections in order: HOME, SERVICES, ABOUT, DEMO REEL, CLIENTS, CONTACT FORM, and social media buttons (Facebook, LinkedIn, Twitter, YouTube, Instagram). Contact: 615-482-9031 info@pelwickdronesolutions.example Smyrna, TN
• Sitemap:
• 6 pages: Home, Inspections, Mapping, Training, Consulting, About
• HOME (Landing Page)
• • Header with logo and tab links (Home, Services, About, Contact)
• • 'CAPTURE. PROCESS. DELIVER.' tagline and 'CONTACT US' button displayed within aerial image of drone over city or construction site
• • Services section with icons, text and read more link to page
• • About section with photo and text with three icons for SAFE. LEGAL. INSURED.
• • Demo reel
• • Clients logos shown scrolling horizontally
• • Contact form
• • Footer with logo, phone, email, social media buttons
• SERVICES (4 different pages)
• • Inspections
• • Mapping
• • Consulting
• • Training
• ABOUT page
• • Company
• • Partners
• • Certifications & Associations
• • Careers
• CONTACT linked to bottom of landing page
• Would you like to receive the newsletter? Yes or No Drop-down list
Nice to have
• Photos of Orvex Talvan or Quillon inspecting infrastructure, buildings, construction sites, etc. A photo of one or two pilots in vest and helmet. Free stock photos preferred but would purchase the right photo that's more relevant.
• website references:
• https://www.brastelmoor.example/
• https://www.kestrimundo.example/services
• https://www.norblat.example/
• http://fenwoprisma.example/
• http://lumtorrex.example/
• http://gavrinoth.example/
• https://www.murbex.example/
Should not have
• not an aerial photography or videography service business, no blog or newsletter

```html
<!DOCTYPE html>
<html lang="en">
<head>
<meta charset="utf-8">
<title>Pelwick Drone Solutions</title>
<link href="https://fonts.googleapis.com/css2?family=Montserrat:wght@400;600;700;800&family=Open+Sans:wght@400;600;700&display=swap" rel="stylesheet">
<style>
:root{
  --blue:#1a8fe0;
  --blue-dark:#0f78c4;
  --ink:#1f1f1f;
  --panel-dark:#1e1e1e;
  --text:#555;
  --grey-bg:#efefef;
  --white:#fff;
  --rule:#d8d8d8;
}
*{box-sizing:border-box;margin:0;padding:0}
html,body{width:1200px;height:2980px;overflow:hidden;background:var(--white)}
body{font-family:"Open Sans",Arial,sans-serif;color:var(--text)}
.page{position:relative;width:1200px;height:2980px;overflow:hidden}
.abs{position:absolute}

/* header */
.site-header{left:0;top:0;width:1200px;height:88px;background:var(--white);box-shadow:0 2px 6px rgba(0,0,0,.08);z-index:5}
.brand{left:60px;top:26px;font-family:"Montserrat",Arial,sans-serif;font-weight:800;font-size:26px;color:var(--ink);letter-spacing:.5px;display:flex;align-items:center;gap:10px}
.brand-dot{width:16px;height:16px;background:var(--blue);border-radius:50%}
.main-nav{right:60px;top:34px;display:flex;gap:34px;align-items:center;font-family:"Montserrat",Arial,sans-serif;font-size:14px;font-weight:600;color:#444}
.main-nav .active{color:var(--blue)}
.nav-social{display:flex;gap:12px}
.nav-social span{width:12px;height:12px;border-radius:50%;background:#444;display:block}

/* hero */
.hero{left:0;top:88px;width:1200px;height:447px;background:linear-gradient(180deg,#b9cfe0 0%,#d6dee3 45%,#9aa59a 70%,#6e7560 100%)}
.hero-drone{left:590px;top:60px;width:560px;height:250px;background:radial-gradient(ellipse at 50% 45%,rgba(40,40,40,.55),rgba(40,40,40,0) 70%)}
.hero-copy{left:170px;top:110px}
.hero-copy h1{font-family:"Montserrat",Arial,sans-serif;font-weight:800;font-size:52px;line-height:58px;color:var(--white);letter-spacing:2px;text-shadow:0 2px 8px rgba(0,0,0,.3)}
.btn{display:inline-block;font-family:"Montserrat",Arial,sans-serif;font-weight:700;font-size:15px;letter-spacing:1.5px;color:var(--white);background:var(--blue);padding:12px 36px}
.hero-copy .btn{margin-top:28px}

/* about */
.about-photo{left:68px;top:590px;width:400px;height:350px;background:linear-gradient(135deg,#9ea9b0,#c9d0d4 50%,#7f8a73);box-shadow:0 4px 12px rgba(0,0,0,.2)}
.about-copy{left:520px;top:615px;width:620px}
.section-title{font-family:"Montserrat",Arial,sans-serif;font-weight:700;font-size:38px;color:var(--ink);letter-spacing:1px}
.about-copy p{font-size:14px;line-height:21px;margin-top:16px}
.read-more{font-weight:700;color:var(--ink);text-decoration:underline}
.badges{display:flex;gap:80px;margin-top:30px;padding-left:50px}
.badge{text-align:center;font-family:"Montserrat",Arial,sans-serif;font-weight:700;font-size:13px;color:var(--ink)}
.badge svg{display:block;margin:0 auto 8px}

/* services */
.services-band{left:0;top:1040px;width:1200px;height:1560px;background:var(--grey-bg)}
.services-title{left:0;top:1070px;width:1200px;text-align:center}
.services-title h2{font-family:"Montserrat",Arial,sans-serif;font-weight:700;font-size:34px;color:var(--ink);letter-spacing:1px}
.title-rule{left:150px;top:1128px;width:900px;height:1px;background:var(--rule)}
.svc-photo{box-shadow:0 4px 10px rgba(0,0,0,.18)}
.svc-card{padding:32px 36px;color:var(--white);box-shadow:0 4px 10px rgba(0,0,0,.18)}
.svc-card.blue{background:var(--blue)}
.svc-card.dark{background:var(--panel-dark)}
.svc-card h3{font-family:"Montserrat",Arial,sans-serif;font-weight:700;font-size:21px;margin-bottom:14px}
.svc-card p{font-size:14px;line-height:21px;color:rgba(255,255,255,.92)}
.svc-card .read-more{color:var(--white)}

/* contact footer */
.contact-band{left:0;top:2600px;width:1200px;height:348px;background:var(--blue)}
.contact-form{left:86px;top:2625px;width:560px;color:var(--white)}
.band-title{font-family:"Montserrat",Arial,sans-serif;font-weight:700;font-size:20px;color:var(--white);letter-spacing:.5px}
.field{background:var(--blue-dark);border:1px solid rgba(255,255,255,.25);height:44px;margin-top:12px;font-size:13px;padding:12px 16px 0;color:rgba(255,255,255,.85)}
.field.tall{height:86px}
.btn-dark{margin-top:14px;background:var(--panel-dark);color:var(--white);font-family:"Montserrat",Arial,sans-serif;font-weight:700;font-size:13px;padding:10px 22px;display:inline-block;letter-spacing:1px}
.contact-info{left:790px;top:2625px;width:340px}
.info-row{display:flex;align-items:center;gap:16px;margin-top:18px;color:var(--white);font-size:13px;line-height:18px}
.info-icon{width:32px;height:32px;border-radius:50%;background:var(--panel-dark);display:flex;align-items:center;justify-content:center;flex-shrink:0}
.social-title{margin-top:30px}
.social-row{display:flex;gap:14px;margin-top:14px}
.social-row span{width:36px;height:36px;border-radius:50%;background:var(--panel-dark);display:block}
.copyright{left:0;top:2948px;width:1200px;height:32px;background:var(--panel-dark);color:#bbb;font-size:12px;text-align:center;line-height:32px}
</style>
</head>
<body>
<div class="page">

  <header class="site-header abs">
    <div class="brand abs"><span class="brand-dot"></span>Pelwick Drone Solutions</div>
    <nav class="main-nav abs">
      <span class="active">HOME</span>
      <span>ABOUT US</span>
      <span>SERVICES</span>
      <span>CONTACT US</span>
      <span class="nav-social"><span></span><span></span><span></span></span>
    </nav>
  </header>

  <section class="hero abs" role="img" aria-label="Aerial view of a city skyline with a drone hovering above">
    <div class="hero-drone abs"></div>
    <div class="hero-copy abs">
      <h1>CAPTURE<br>PROCESS<br>DELIVER</h1>
      <span class="btn">CONTACT US</span>
    </div>
  </section>

  <div class="about-photo abs" role="img" aria-label="Pilot in hard hat and safety vest flying a drone beside high-rise construction"></div>
  <section class="about-copy abs">
    <h2 class="section-title">ABOUT US</h2>
    <p>Pelwick Drone Solutions provides turnkey solutions to capture, process, and deliver actionable data to customers. Our company performs inspections, mapping, consulting and training for businesses operating in telecommunications, energy utilities, construction, insurance and government sectors.</p>
    <p>Our team is certified, insured and operates safely in accordance with FAA regulations. Pelwick Drone Solutions offers a suite of solutions using the latest technology in unmanned aerial systems. <span class="read-more">READ MORE</span></p>
    <div class="badges">
      <div class="badge">
        <svg width="40" height="40" viewBox="0 0 40 40"><circle cx="20" cy="20" r="17" fill="none" stroke="#1f1f1f" stroke-width="3"/><path d="M12 20l6 6 11-12" fill="none" stroke="#1f1f1f" stroke-width="3.5" stroke-linecap="round" stroke-linejoin="round"/></svg>
        SAFE
      </div>
      <div class="badge">
        <svg width="40" height="40" viewBox="0 0 40 40"><path d="M20 4l14 6v9c0 9-6 15-14 18C12 34 6 28 6 19v-9z" fill="#1f1f1f"/><path d="M14 20l5 5 8-9" fill="none" stroke="#fff" stroke-width="3" stroke-linecap="round" stroke-linejoin="round"/></svg>
        LEGAL
      </div>
      <div class="badge">
        <svg width="40" height="40" viewBox="0 0 40 40"><rect x="7" y="10" width="26" height="24" rx="3" fill="none" stroke="#1f1f1f" stroke-width="3"/><path d="M14 10V7h12v3M13 21h14M13 27h10" stroke="#1f1f1f" stroke-width="3" fill="none"/></svg>
        INSURED
      </div>
    </div>
  </section>

  <div class="services-band abs"></div>
  <div class="services-title abs"><h2>PROFESSIONAL SERVICES</h2></div>
  <div class="title-rule abs"></div>

  <!-- Inspections -->
  <div class="svc-photo abs" style="left:80px;top:1160px;width:470px;height:290px;background:linear-gradient(160deg,#b88e73,#d9c2ae 55%,#8f9ca4)" role="img" aria-label="Drone on a rooftop inspecting roof tiles"></div>
  <div class="svc-card blue abs" style="left:530px;top:1200px;width:580px;height:220px">
    <h3>Inspections</h3>
    <p>Lorem Ipsum is simply dummy text of the printing and typesetting industry. Lorem Ipsum has been the industry's standard dummy text ever since the 1500s, when an unknown printer took a galley of type and scrambled it to make a type specimen book. <span class="read-more">READ MORE</span></p>
  </div>

  <!-- Mapping -->
  <div class="svc-photo abs" style="left:560px;top:1510px;width:550px;height:270px;background:linear-gradient(150deg,#8fb3d6,#c7d6e1 45%,#d77a3a 75%,#6f7a80)" role="img" aria-label="Engineer in hard hat operating a drone over a construction site"></div>
  <div class="svc-card dark abs" style="left:80px;top:1590px;width:520px;height:220px">
    <h3>Mapping</h3>
    <p>Lorem Ipsum is simply dummy text of the printing and typesetting industry. Lorem Ipsum has been the industry's standard dummy text ever since the 1500s, when an unknown printer took a galley of type and scrambled it to make a type specimen book. <span class="read-more">READ MORE</span></p>
  </div>

  <!-- Consulting -->
  <div class="svc-photo abs" style="left:80px;top:1870px;width:470px;height:290px;background:linear-gradient(135deg,#e4e6e8,#c4b8ad 50%,#6f7780)" role="img" aria-label="Two consultants shaking hands in an office meeting"></div>
  <div class="svc-card blue abs" style="left:530px;top:1920px;width:580px;height:220px">
    <h3>Consulting</h3>
    <p>Lorem Ipsum is simply dummy text of the printing and typesetting industry. Lorem Ipsum has been the industry's standard dummy text ever since the 1500s, when an unknown printer took a galley of type and scrambled it to make a type specimen book. <span class="read-more">READ MORE</span></p>
  </div>

  <!-- Training -->
  <div class="svc-photo abs" style="left:610px;top:2230px;width:500px;height:290px;background:linear-gradient(140deg,#e6e2da,#9a9690 50%,#3f4448)" role="img" aria-label="Trainee technicians working on a drone in a workshop"></div>
  <div class="svc-card dark abs" style="left:80px;top:2270px;width:560px;height:220px">
    <h3>Training</h3>
    <p>Lorem Ipsum is simply dummy text of the printing and typesetting industry. Lorem Ipsum has been the industry's standard dummy text ever since the 1500s, when an unknown printer took a galley of type and scrambled it to make a type specimen book. <span class="read-more">READ MORE</span></p>
  </div>

  <!-- Contact -->
  <div class="contact-band abs"></div>
  <form class="contact-form abs">
    <h2 class="band-title">CONTACT FORM</h2>
    <div class="field">Name</div>
    <div class="field">Email</div>
    <div class="field tall">Message</div>
    <span class="btn-dark">SUBMIT</span>
  </form>

  <section class="contact-info abs">
    <h2 class="band-title">CONTACT INFO</h2>
    <div class="info-row">
      <span class="info-icon"><svg width="14" height="16" viewBox="0 0 14 16"><path d="M7 0a6 6 0 0 0-6 6c0 4.5 6 10 6 10s6-5.5 6-10a6 6 0 0 0-6-6z" fill="#fff"/><circle cx="7" cy="6" r="2.2" fill="#1e1e1e"/></svg></span>
      <span>4820 Brennick Way, Harlowe, OR 97381<br>United States</span>
    </div>
    <div class="info-row">
      <span class="info-icon"><svg width="14" height="14" viewBox="0 0 14 14"><path d="M3 0l3 3-2 2a9 9 0 0 0 5 5l2-2 3 3-2 3C6 14 0 8 0 3z" fill="#fff"/></svg></span>
      <span>615-482-9031</span>
    </div>
    <div class="info-row">
      <span class="info-icon"><svg width="16" height="12" viewBox="0 0 16 12"><rect width="16" height="12" rx="1" fill="#fff"/><path d="M1 1l7 6 7-6" fill="none" stroke="#1e1e1e" stroke-width="1.5"/></svg></span>
      <span>info@pelwickdronesolutions.example</span>
    </div>
    <h2 class="band-title social-title">SOCIAL LINKS</h2>
    <div class="social-row"><span></span><span></span><span></span></div>
  </section>

  <footer class="copyright abs">Pelwick Drone Solutions © 2017 &nbsp;·&nbsp; All Rights Reserved</footer>
</div>
</body>
</html>
```